Martin Hale PA Card Logo

Current logo attached. Its 25 year old logo I have used. Looking for a new fresh elegant professional look/design for a law firm that has high net worth clientele and is estate planning business law firm. Firm mis in Palm Beach Florida.
One sided card linen stock white will be used. Logo section name section. Logo should include nice elegant design using the letter "M" perhapa (I am not wed to current font of the M on current logo.) Be creative there with logo design. My initials are MH.......color scheme I figure 3 tone... Raised Gold Foil, Blue name of firm = Martin Hale, P.A. My practice focus is Family and Business Asset Protection. My name is Martin M. Hale, Esq. Practice specialties include Asset Protection trusts, Business Succession Planning, LLC law, Estate Planning, Medicaid Planning (Maybe put those topics in bullets in a section of card. Bottom of card can be reserved smaller print address phone website and email address. Address section is not as important as logo and topics of practice on front. I foresee address section can be in dark blue. MY name and Topics dark blue as well.
Target Market(s)
affluent; business owners executives; wealth 2-10 million net worth
Industry/Entity Type
business law and estate planning
Contact Information for Business Card
White thick linen one sided

```html
<!DOCTYPE html>
<html lang="en">
<head>
<meta charset="utf-8">
<title>Martin Hale, P.A. — Business Card</title>
<link rel="stylesheet" href="https://fonts.googleapis.com/css2?family=Carlito&family=Figtree:wght@600&display=swap">
<style>
  :root {
    --backdrop: #9b9b9b;
    --paper: #ffffff;
    --navy: #062d54;
    --gold: #b8892f;
    --ink: #1f2a36;
    --white: #ffffff;
  }
  * { box-sizing: border-box; margin: 0; padding: 0; }
  html, body { width: 1093px; height: 1200px; overflow: hidden; }
  body { background: var(--backdrop); position: relative; font-family: "Carlito", "Calibri", sans-serif; }

  .card { position: absolute; left: 264px; width: 580px; height: 356px; border-radius: 24px; overflow: hidden; }
  .card--front { top: 226px; background: var(--paper); }
  .card--back { top: 621px; background: var(--navy); }

  .accent-bar { position: absolute; left: 0; top: 38px; width: 12px; height: 42px; background: var(--navy); }
  .attorney-name { position: absolute; left: 27px; top: 36px; font-family: "Figtree", sans-serif; font-weight: 600; font-size: 23px; color: var(--navy); letter-spacing: -0.3px; }
  .practice-focus { position: absolute; left: 29px; top: 64px; font-size: 16px; color: var(--navy); }

  .firm-mark { position: absolute; right: 35px; top: 30px; display: flex; flex-direction: column; align-items: flex-end; }
  .firm-mark__dot { width: 74px; height: 74px; border-radius: 50%; background: var(--gold); margin: 0 62px 20px 0; }
  .firm-name { font-family: "Figtree", sans-serif; font-weight: 600; font-size: 29px; color: var(--navy); letter-spacing: -0.5px; white-space: nowrap; }

  .specialties { position: absolute; left: 25px; top: 168px; list-style: none; }
  .specialties li { font-size: 16.5px; line-height: 21px; color: var(--ink); display: flex; align-items: center; }
  .specialties li::before { content: ""; width: 7px; height: 7px; border-radius: 50%; background: var(--gold); margin-right: 7px; }

  .contact-row { position: absolute; left: 27px; top: 288px; display: flex; gap: 14px; font-size: 16px; color: var(--ink); }
  .contact-row span { display: flex; align-items: center; gap: 5px; }
  .contact-row svg { width: 19px; height: 19px; }

  .address-band { position: absolute; left: 0; bottom: 0; width: 100%; height: 39px; background: var(--navy); color: var(--white); font-size: 16px; display: flex; align-items: center; justify-content: center; }

  .back-mark { position: absolute; inset: 0; display: flex; flex-direction: column; align-items: center; justify-content: center; padding-top: 20px; }
  .back-mark__dot { width: 110px; height: 110px; border-radius: 50%; background: var(--gold); margin-bottom: 34px; }
  .back-mark .firm-name { color: var(--white); font-size: 37px; }
</style>
</head>
<body>
  <section class="card card--front">
    <div class="accent-bar"></div>
    <h1 class="attorney-name">Martin M. Hale, Esq.</h1>
    <p class="practice-focus">Family and Business Asset Protection</p>

    <div class="firm-mark">
      <div class="firm-mark__dot"></div>
      <div class="firm-name">Martin Hale, P.A.</div>
    </div>

    <ul class="specialties">
      <li>Asset Protection trusts</li>
      <li>Business Succession Planning</li>
      <li>LLC Law</li>
      <li>Estate Planning</li>
      <li>Medicaid Planning</li>
    </ul>

    <div class="contact-row">
      <span>
        <svg viewBox="0 0 20 20" fill="none" stroke="#062d54" stroke-width="1.4"><circle cx="10" cy="10" r="8.8"/><path d="M7 5.5l1.6 2.3-1 1c.6 1.4 1.6 2.4 3 3l1-1 2.3 1.6-1 1.6c-3.3-.2-6.4-3.3-6.6-6.6z" fill="#062d54"/></svg>
        561-555 0142
      </span>
      <span>
        <svg viewBox="0 0 20 20" fill="none" stroke="#062d54" stroke-width="1.4"><circle cx="10" cy="10" r="8.8"/><rect x="5.5" y="7" width="9" height="6.2" fill="#062d54"/><path d="M5.5 7l4.5 3.4L14.5 7" stroke="#fff" stroke-width="0.9"/></svg>
        info@mhalepa.com
      </span>
      <span>
        <svg viewBox="0 0 20 20" fill="none" stroke="#062d54" stroke-width="1.2"><circle cx="10" cy="10" r="8.8"/><circle cx="10" cy="10" r="5.5"/><ellipse cx="10" cy="10" rx="2.3" ry="5.5"/><path d="M4.5 10h11M5.3 7.3h9.4M5.3 12.7h9.4"/></svg>
        www.mhalepa.com
      </span>
    </div>

    <div class="address-band">214 Royal Palm Way, Palm Beach, FL 33480</div>
  </section>

  <section class="card card--back">
    <div class="back-mark">
      <div class="back-mark__dot"></div>
      <div class="firm-name">Martin Hale, P.A.</div>
    </div>
  </section>
</body>
</html>
```